Business Card Design Project

Professional business cards for law firm - a rough example of what we are looking for is attached. The logo, colour and styling of the name are all new and dont need to be changed. We need layout for front and back. We are looking for some imaginative layout of info. We are a young vibrant firm and not too conservative and are not adverse to something quite different.
Updates

Thank you for all the submissions.  We have been blown away with the quality of your work.  Our management team will be meeting later in the week to make our decision.  Again, thanks for the fabulous work.

Industry/Entity Type

Conservative

Requirements
Must have
• Logo and name as in attached example (colour and font)
Should not have
• Scales of Justice

```html
<!DOCTYPE html>
<html lang="en">
<head>
<meta charset="utf-8">
<title>Marlow Price Legal – Business Cards</title>
<link rel="stylesheet" href="https://fonts.googleapis.com/css2?family=Source+Sans+3:ital,wght@0,400;0,500;0,600;1,400&display=swap">
<style>
  :root {
    --page-bg: #e4dfd7;
    --card-black: #050505;
    --brand-green: #637f37;
    --band-green: #6a863d;
    --text-white: #f4f4f4;
    --text-grey: #8a8a8a;
    --rule-grey: #bdbdbd;
    --swoosh-white: #ffffff;
    --ring-grey: #5a5a5a;
  }
  * { margin: 0; padding: 0; box-sizing: border-box; }
  html, body {
    width: 1200px; height: 1067px; overflow: hidden;
    background: var(--page-bg);
    font-family: "Source Sans 3", Arial, sans-serif;
  }
  .card {
    position: absolute;
    width: 747px; height: 428px;
    border-radius: 32px;
    background: var(--card-black);
    overflow: hidden;
    color: var(--text-white);
  }
  .card--front { left: 67px; top: 68px; }
  .card--back { left: 300px; top: 551px; }
  .swoosh { position: absolute; left: 0; top: 0; width: 747px; height: 428px; }

  .wordmark { position: absolute; text-align: center; color: var(--brand-green); font-weight: 500; }
  .wordmark__name { font-size: 48px; line-height: 1; letter-spacing: 0.5px; }
  .wordmark__legal { font-size: 28px; line-height: 1; letter-spacing: 5px; margin-top: 8px; }
  .tagline { position: absolute; font-style: italic; font-size: 18px; color: var(--text-grey); white-space: nowrap; }

  .card--front .wordmark { left: 0; width: 747px; top: 24px; }
  .card--front .tagline { left: 0; width: 747px; text-align: center; top: 130px; }

  .services { position: absolute; top: 186px; font-size: 16px; line-height: 26.7px; list-style: none; }
  .services--left { left: 28px; }
  .services--right { left: 170px; width: 175px; text-align: right; }

  .divider { position: absolute; left: 378px; top: 187px; width: 1px; height: 93px; background: var(--rule-grey); }

  .contact { position: absolute; left: 400px; top: 184px; font-size: 15.5px; list-style: none; line-height: 1.25; }
  .contact li { display: flex; align-items: center; margin-bottom: 7px; }
  .contact li.plain { margin-bottom: 2px; }
  .contact svg { width: 13px; height: 13px; margin-right: 9px; flex: none; fill: var(--text-white); }

  .card--back .emblem { position: absolute; left: 129px; top: 76px; width: 194px; height: 194px; border: 3px solid var(--ring-grey); border-radius: 50%; }
  .card--back .wordmark { left: 340px; width: 300px; top: 120px; }
  .card--back .tagline { left: 340px; width: 300px; text-align: center; top: 216px; }

  .person { position: absolute; right: 46px; top: 358px; text-align: center; }
  .person__name { font-size: 20px; font-weight: 600; }
  .person__role { font-size: 15px; margin-top: 4px; }
</style>
</head>
<body>

<section class="card card--front">
  <svg class="swoosh" viewBox="0 0 747 428" aria-hidden="true">
    <path d="M0 360 C 250 345, 500 322, 747 318" fill="none" stroke="var(--band-green)" stroke-width="6"/>
    <path d="M170 428 C 380 390, 560 334, 747 330 L747 428 Z" fill="var(--band-green)"/>
    <path d="M0 384 C 160 390, 360 372, 480 348 C 360 386, 210 418, 80 428 L0 428 Z" fill="var(--swoosh-white)"/>
  </svg>

  <div class="wordmark">
    <div class="wordmark__name">Marlow Price</div>
    <div class="wordmark__legal">LEGAL</div>
  </div>
  <p class="tagline">guiding you toward a clear path</p>

  <ul class="services services--left">
    <li>Family</li>
    <li>Restraining Order</li>
    <li>Probate/Wills</li>
    <li>Dividing Fences</li>
  </ul>
  <ul class="services services--right">
    <li>Traffic</li>
    <li>Criminal</li>
    <li>Debt Recovery</li>
    <li>Financial Agreements</li>
  </ul>

  <div class="divider"></div>

  <ul class="contact">
    <li class="plain">4/27 Carrow Street, Ashdale WA 6107</li>
    <li>PO Box 312, Ashdale WA 6981</li>
    <li>
      <svg viewBox="0 0 16 16" aria-hidden="true"><path d="M3.5 1 L6 4 L4.5 6 C5.5 8 8 10.5 10 11.5 L12 10 L15 12.5 L13 15 C7 14.5 1.5 9 1 3 Z"/></svg>
      9400 5127, 6100 3384
    </li>
    <li>
      <svg viewBox="0 0 16 16" aria-hidden="true"><rect x="4" y="1" width="8" height="5"/><rect x="1" y="6" width="14" height="7" rx="1"/><rect x="4" y="11" width="8" height="4" fill="var(--card-black)"/></svg>
      6300 4419
    </li>
    <li>
      <svg viewBox="0 0 16 16" aria-hidden="true"><path d="M1 3 H15 V13 H1 Z M1.5 3.5 L8 9 L14.5 3.5" fill="var(--text-white)" stroke="var(--card-black)" stroke-width="1.2"/></svg>
      reception@marlowpricelegal.com.au
    </li>
  </ul>
</section>

<section class="card card--back">
  <svg class="swoosh" viewBox="0 0 747 428" aria-hidden="true">
    <path d="M0 358 C 250 342, 500 320, 747 316" fill="none" stroke="var(--band-green)" stroke-width="6"/>
    <path d="M200 428 C 400 390, 570 332, 747 328 L747 428 Z" fill="var(--band-green)"/>
    <path d="M0 382 C 160 390, 360 372, 470 350 C 350 388, 210 418, 80 428 L0 428 Z" fill="var(--swoosh-white)"/>
  </svg>

  <div class="emblem"></div>

  <div class="wordmark">
    <div class="wordmark__name">Marlow Price</div>
    <div class="wordmark__legal">LEGAL</div>
  </div>
  <p class="tagline">guiding you toward a clear path</p>

  <div class="person">
    <div class="person__name">Clara Whitfield LLB BA</div>
    <div class="person__role">Solicitor</div>
  </div>
</section>

</body>
</html>
```